Kestra Rowe - Contact/Landing Page

I need a landing page which will essentially be the page that customers will go to from the 'website' link on TLX listing. It will provide a short overview of services which need to be selectable. a little further down can capture some contact details followed by a large Submit Now button etc...

I have some icon/logo's that can be utilised at the bottom of the page as industry type references.

Target Market(s)

End of Lease Cleaning Services

Industry/Entity Type

Cleaning Service

Colors

Designer to choose colors to be used in the design.

Requirements
Must have
• As per description
Should not have
• Colours to match my website kestrarowe.com.au

```html
<!DOCTYPE html>
<html lang="en">
<head>
<meta charset="utf-8">
<title>Kestra Rowe – End of Lease Cleaning</title>
<link href="https://fonts.googleapis.com/css2?family=Bebas+Neue&family=Lora:wght@400&display=swap" rel="stylesheet">
<style>
:root{
  --blue:#1aa3dc;
  --blue-deep:#2f6fb6;
  --hero-a:#4f86c8;
  --hero-b:#3a74bd;
  --ink:#222426;
  --text:#2b2b2b;
  --white:#ffffff;
  --panel:rgba(33,122,160,.82);
  --footer:#f2f2f2;
  --rule:#dcdcdc;
}
*{box-sizing:border-box;margin:0;padding:0}
html,body{width:1200px;height:2302px;overflow:hidden;background:var(--white)}
body{position:relative;font-family:'Lora',serif;color:var(--text)}
.display{font-family:'Bebas Neue',sans-serif;letter-spacing:1px}

/* Hero */
.hero{position:absolute;left:0;top:0;width:1200px;height:662px}
.hero-photo{position:absolute;inset:0 0 62px 0;background:linear-gradient(180deg,var(--hero-a),var(--hero-b) 60%,#4b84c6)}
.hero-wave{position:absolute;left:0;top:560px;width:1200px;height:102px}
.brand{position:absolute;top:190px;left:0;width:1200px;display:flex;justify-content:center;align-items:center;gap:16px}
.brand-dot{width:54px;height:54px;border-radius:50%;background:var(--white)}
.brand-name{font-family:'Bebas Neue',sans-serif;font-size:64px;color:var(--white);letter-spacing:2px;line-height:1}
.hero-title{position:absolute;top:400px;width:1200px;text-align:center;color:var(--white);font-size:78px;line-height:1;letter-spacing:2px}
.hero-rule{position:absolute;top:497px;left:476px;width:262px;height:1px;background:rgba(255,255,255,.85)}
.hero-sub{position:absolute;top:504px;width:1236px;text-align:center;color:var(--white);font-size:31px}

/* Services */
.services-title{position:absolute;top:754px;width:1200px;text-align:center;font-size:66px;color:var(--ink);line-height:1}
.card{position:absolute;top:876px;width:308px;height:404px}
.card svg.roof{position:absolute;left:0;top:0}
.card-ring{position:absolute;left:6px;top:92px;width:296px;height:296px;border-radius:50%;background:var(--white);box-shadow:0 8px 18px rgba(0,0,0,.08),0 0 0 4px #f4f4f4}
.card-circle{position:absolute;left:14px;top:100px;width:280px;height:280px;border-radius:50%;border:2px solid var(--blue);background:var(--white);text-align:center;padding:56px 18px 0}
.card-title{font-size:37px;color:var(--ink);line-height:1}
.card-text{font-size:17.5px;line-height:27px;margin-top:8px;height:84px}
.select{display:inline-flex;align-items:center;gap:10px;font-size:16.5px;margin-top:6px}
.box{width:20px;height:20px;border:1px solid #555;display:inline-block;position:relative}

/* Contact */
.contact{position:absolute;left:0;top:1378px;width:1200px;height:641px;overflow:hidden}
.contact-photo{position:absolute;inset:0;background:linear-gradient(100deg,#1f2123 0%,#2d3033 45%,#4a4d50 75%,#3b3e41 100%)}
.contact-watermark{position:absolute;top:-30px;left:0;width:1200px;text-align:center;font-size:290px;color:rgba(255,255,255,.05);letter-spacing:12px;line-height:1}
.contact-title{position:absolute;top:68px;width:1200px;text-align:center;color:var(--white);font-size:66px;line-height:1}
.form{position:absolute;left:214px;top:166px;width:772px;height:420px;background:var(--panel);padding:32px 30px}
.field{position:absolute;background:var(--white);font-size:17px;color:#444;padding:16px 18px;height:54px}
.btn{position:absolute;left:30px;top:337px;width:712px;height:54px;background:var(--ink);color:var(--white);font-size:25px;display:flex;align-items:center;justify-content:center;letter-spacing:1px}

/* Footer */
.footer{position:absolute;left:0;top:2019px;width:1200px;height:283px;background:var(--footer)}
.badge{position:absolute;top:62px;width:178px;height:90px;background:var(--white);border:1px solid #e2e2e2;box-shadow:0 1px 4px rgba(0,0,0,.08);display:flex;align-items:center;justify-content:center}
.badge span{display:block;width:130px;height:44px;border-radius:6px}
.licence{position:absolute;top:176px;width:1200px;text-align:center;font-size:18px}
.footer-rule{position:absolute;top:224px;left:113px;width:975px;height:1px;background:var(--rule)}
.copyright{position:absolute;top:243px;width:1200px;text-align:center;font-size:15px}
</style>
</head>
<body>

<header class="hero">
  <div class="hero-photo" role="img" aria-label="Blurred house exterior with pest close-up, blue tinted"></div>
  <svg class="hero-wave" viewBox="0 0 1200 102" width="1200" height="102">
    <path d="M0 38 C250 38 450 100 620 100 C800 100 960 38 1200 38 L1200 102 L0 102Z" fill="var(--blue)"/>
    <path d="M0 0 L1200 0 L1200 36 C960 36 800 94 620 94 C450 94 250 36 0 36Z" fill="#4b84c6"/>
    <path d="M0 40 C250 40 450 98 620 98 C800 98 960 40 1200 40 L1200 102 L0 102Z" fill="var(--white)" transform="translate(0,6)"/>
  </svg>
  <div class="brand"><span class="brand-dot"></span><span class="brand-name">Kestra Rowe</span></div>
  <h1 class="hero-title display">End of Lease Cleaning</h1>
  <div class="hero-rule"></div>
  <p class="hero-sub">Licensed Pest Control</p>
</header>

<h2 class="services-title display">End of Lease Services</h2>

<section class="card" style="left:112px">
  <svg class="roof" width="308" height="140" viewBox="0 0 308 140">
    <path d="M154 0 L306 112 L266 112 L266 150 L42 150 L42 112 L2 112Z" fill="var(--ink)"/>
    <g fill="var(--blue)"><path d="M128 50 h26 l-4 26 h-18z"/><rect x="138" y="24" width="3" height="26"/><rect x="168" y="24" width="3" height="40"/><path d="M158 64 h22 v12 h-22z"/></g>
  </svg>
  <div class="card-ring"></div>
  <div class="card-circle">
    <h3 class="card-title display">Cleaning</h3>
    <p class="card-text">All intirior cleaning carried out to property management requirements.</p>
    <label class="select"><span class="box"><svg width="20" height="20" viewBox="0 0 20 20"><path d="M4 10 L8 15 L16 3" stroke="#222" stroke-width="2.4" fill="none"/></svg></span>Select This</label>
  </div>
</section>

<section class="card" style="left:446px">
  <svg class="roof" width="308" height="140" viewBox="0 0 308 140">
    <path d="M154 0 L306 112 L266 112 L266 150 L42 150 L42 112 L2 112Z" fill="var(--ink)"/>
    <g fill="var(--blue)"><rect x="130" y="40" width="48" height="10"/><rect x="130" y="54" width="48" height="10"/><rect x="130" y="68" width="48" height="8"/><rect x="152" y="30" width="26" height="8"/><rect x="126" y="40" width="3" height="36"/></g>
  </svg>
  <div class="card-ring"></div>
  <div class="card-circle">
    <h3 class="card-title display">Carpet Cleaning</h3>
    <p class="card-text">Carpet stoam cleaning to Australian standard as 3733:1995</p>
    <label class="select"><span class="box"></span>Select This</label>
  </div>
</section>

<section class="card" style="left:780px">
  <svg class="roof" width="308" height="140" viewBox="0 0 308 140">
    <path d="M154 0 L306 112 L266 112 L266 150 L42 150 L42 112 L2 112Z" fill="var(--ink)"/>
    <g fill="var(--blue)"><rect x="148" y="38" width="28" height="38" rx="4"/><rect x="128" y="48" width="8" height="28" rx="2"/></g>
    <circle cx="162" cy="60" r="8" fill="none" stroke="var(--ink)" stroke-width="2.5"/><path d="M156 66 L168 54" stroke="var(--ink)" stroke-width="2.5"/>
  </svg>
  <div class="card-ring"></div>
  <div class="card-circle">
    <h3 class="card-title display">Pest Control</h3>
    <p class="card-text">Mandatory requirement for pest on premises</p>
    <label class="select"><span class="box"></span>Select This</label>
  </div>
</section>

<section class="contact">
  <div class="contact-photo" role="img" aria-label="Pest technician in protective suit spraying, dark monochrome"></div>
  <div class="contact-watermark display">Contact Us</div>
  <h2 class="contact-title display">Contact Us</h2>
  <form class="form">
    <div class="field" style="left:30px;top:32px;width:349px">First Name</div>
    <div class="field" style="left:393px;top:32px;width:349px">Surname</div>
    <div class="field" style="left:30px;top:100px;width:349px">Email Address</div>
    <div class="field" style="left:393px;top:100px;width:349px">Phone No</div>
    <div class="field" style="left:30px;top:168px;width:712px;height:155px">Subarb</div>
    <div class="btn display">Submit Now !</div>
  </form>
</section>

<footer class="footer">
  <div class="badge" style="left:222px"><span style="background:#2b2b2b"></span></div>
  <div class="badge" style="left:414px"><span style="background:#b8c3dd"></span></div>
  <div class="badge" style="left:607px"><span style="background:#2d5aa6"></span></div>
  <div class="badge" style="left:800px"><span style="background:#8dbb3b"></span></div>
  <p class="licence">Pet Licence: 4810362</p>
  <div class="footer-rule"></div>
  <p class="copyright">Copyright © 2021 Kestra Rowe. All Rights Reserved.</p>
</footer>

</body>
</html>
```